Letterhead for New Orthopaedic Surgery Practice

My husband and I are starting our own practice named RB Spine & Vitality Center. We would like to create a nice simple but high class letterhead that doesn't use too much solid color ink when printing. I like the colors dark blue, gold, yellow. Open to other suggestions. We will need to list him and I both on the top of the letterhead. Here is the important information:
Lucinda Perrow, M.D. - Hand and Upper Extremity Surgery
Abena Quist, M.D. - Hip & Knee Replacement/General Orthopaedic Surgery
Location: 18735 North Harlow Pkwy
Coral Springs, FL 33071
Phone: 954-218-4650
Fax: 954-582-1346
Email: info@myrbspine.com

The only thing is that the phone and fax numbers will change once we get into our space. I just want to get the design started. I am including several documents which are my previous practice letterhead, my current procedure room letterhead, and our new Logo. The other letterheads are just for examples but please think outside of the box! We would love to see some great designs.

Colors
0054AA
0677BA
7BADD7
CADEEF
E8F1F8
0094D4
00A9DD
6FCCEA
C7EBF8
E9F6FB

Requirements
Must have
• class, elegance, luxury

```html
<!DOCTYPE html>
<html lang="en">
<head>
<meta charset="utf-8">
<title>RB Spine &amp; Vitality Center – Letterhead</title>
<link href="https://fonts.googleapis.com/css2?family=Figtree:wght@400;500;600;700&family=Lato:wght@400;700&display=swap" rel="stylesheet">
<style>
  :root {
    --navy: #1b2649;
    --gold: #bf9a55;
    --paper: #ffffff;
    --paper-edge: #ededed;
    --backdrop: #d8d8d8;
    --ink: #1a2540;
    --body-grey: #676767;
    --muted: #6f6f6f;
  }
  * { margin: 0; padding: 0; box-sizing: border-box; }
  html, body { width: 1174px; height: 1200px; overflow: hidden; }
  body { background: var(--backdrop); position: relative; font-family: "Lato", sans-serif; }

  .letterhead {
    position: absolute; left: 136px; top: 20px;
    width: 901px; height: 1160px;
    background: radial-gradient(ellipse at 50% 40%, var(--paper) 40%, var(--paper-edge) 100%);
    box-shadow: 0 6px 14px rgba(0,0,0,.25);
    overflow: hidden;
  }
  .letterhead__waves { position: absolute; inset: 0; width: 100%; height: 100%; }

  .brand-seal {
    position: absolute; left: 80px; top: 21px; width: 160px; height: 160px;
    border-radius: 50%; background: var(--paper);
    display: flex; align-items: center; justify-content: center; text-align: center;
  }
  .brand-seal__name {
    font-family: "Figtree", sans-serif; font-weight: 700; font-size: 17px; line-height: 1.25;
    color: var(--navy); width: 120px;
  }

  .physicians {
    position: absolute; right: 64px; top: 26px; text-align: right;
    font-family: "Figtree", sans-serif; color: #fff;
  }
  .physicians__name { font-weight: 700; font-size: 16px; color: var(--gold); line-height: 22px; }
  .physicians__specialty { font-size: 13.5px; line-height: 20px; margin-bottom: 4px; }

  .recipient { position: absolute; left: 83px; top: 270px; }
  .recipient__name { font-weight: 700; font-size: 18px; color: var(--ink); line-height: 24px; }
  .recipient__title { font-weight: 700; font-size: 13px; color: #111; line-height: 18px; }
  .letter-date { position: absolute; right: 86px; top: 293px; font-size: 13px; color: var(--muted); }

  .letter-body {
    position: absolute; left: 83px; top: 355px; width: 733px;
    font-size: 13.3px; line-height: 21.2px; color: var(--body-grey);
    text-align: justify; hyphens: auto;
  }
  .letter-body p + p { margin-top: 21px; }

  .signature-mark {
    position: absolute; left: 83px; top: 848px; width: 190px; height: 42px;
    background: linear-gradient(90deg, rgba(30,30,30,.12), rgba(30,30,30,.04));
    border-radius: 4px;
  }
  .signatory { position: absolute; left: 83px; top: 916px; }
  .signatory__name { font-weight: 700; font-size: 18px; color: #111; line-height: 24px; }
  .signatory__title { font-weight: 700; font-size: 13px; color: var(--muted); line-height: 18px; }

  .contact-bar {
    position: absolute; left: 0; right: 0; top: 1121px;
    display: flex; justify-content: center; align-items: center; gap: 11px;
    font-family: "Figtree", sans-serif; font-weight: 500; font-size: 14px; color: #fff;
  }
  .contact-bar__item { display: flex; align-items: center; gap: 5px; white-space: nowrap; }
  .contact-bar__icon { width: 13px; height: 13px; fill: var(--gold); }
</style>
</head>
<body>
  <article class="letterhead">
    <svg class="letterhead__waves" viewBox="0 0 1264 1627" preserveAspectRatio="none" aria-hidden="true">
      <path fill="var(--navy)" d="M0 0 H1264 V150 C1050 215 850 170 650 130 C500 100 400 85 300 95 C180 110 80 140 0 165 Z"/>
      <path fill="var(--gold)" d="M0 183 C90 146 190 118 300 108 C420 98 520 116 660 146 C850 186 1030 200 1200 192 C1030 212 850 200 660 160 C520 130 420 114 300 122 C190 132 90 162 0 198 Z"/>
      <path fill="var(--navy)" d="M330 122 C500 120 700 180 900 212 C1050 236 1170 220 1264 178 V212 C1170 244 1050 258 900 234 C700 204 500 142 330 134 Z"/>

      <path fill="var(--navy)" d="M0 1478 C300 1420 700 1440 1130 1505 C700 1462 300 1468 0 1508 Z"/>
      <path fill="var(--gold)" d="M70 1497 C500 1470 900 1532 1264 1452 V1474 C900 1556 500 1494 70 1499 Z"/>
      <path fill="var(--navy)" d="M0 1540 C300 1480 700 1560 1000 1555 C1130 1548 1200 1512 1264 1488 V1627 H0 Z"/>
    </svg>

    <div class="brand-seal">
      <span class="brand-seal__name">RB Spine &amp; Vitality Center</span>
    </div>

    <header class="physicians">
      <div class="physicians__name">Abena Quist, M.D.</div>
      <div class="physicians__specialty">Hip &amp; Knee Replacement / General Orthopaedic Surgery</div>
      <div class="physicians__name">Lucinda Perrow, M.D.</div>
      <div class="physicians__specialty">Hand and Upper Extremity Surgery</div>
    </header>

    <div class="recipient">
      <div class="recipient__name">Dear. Mrs Delia Hart</div>
      <div class="recipient__title">Chief Director</div>
    </div>
    <div class="letter-date">Date: 07-August-2025</div>

    <div class="letter-body">
      <p>Lorem ipsum dolor sit amet, consectetur adipiscing elit, sed do eiusmod tempor incididunt ut labore et dolore magna aliqua. Sollicitudin ac orci phasellus egestas tellus rutrum tellus. Euismod elementum nisi quis eleifend quam adipiscing vitae proin sagittis. Egestas sed tempus urna et pharetra pharetra. Quis blandit turpis cursus in hac habitasse. Sed velit dignissim sodales ut eu. Ac auctor augue mauris augue neque. In arcu cursus euismod quis viverra nibh cras pulvinar mattis. Libero justo laoreet sit amet. Felis eget nunc lobortis mattis aliquam faucibus purus in. Pulvinar etiam non quam lacus suspendisse faucibus. Odio tempor orci dapibus ultrices. Velit dignissim sodales ut eu sem integer vitae justo. Fermentum et sollicitudin ac orci phasellus egestas. Pharetra vel turpis nunc eget lorem dolor sed. Sed turpis tincidunt id aliquet risus feugiat in ante. Mus mauris vitae ultricies leo integer malesuada nunc vel. Rhoncus urna neque viverra justo nec ultrices dui. Ut placerat orci nulla pellentesque dignissim enim sit amet.</p>
      <p>Bibendum arcu vitae elementum curabitur vitae nunc. Nunc pulvinar sapien et ligula ullamcorper malesuada. At elementum eu facilisis sed. Erat pellentesque adipiscing commodo elit at imperdiet dui accumsan sit. Nunc scelerisque viverra mauris in aliquam sem fringilla. In vitae turpis massa sed. Volutpat ac tincidunt vitae semper quis lectus nulla at. Massa placerat duis ultricies lacus sed turpis. Dui vivamus arcu felis bibendum ut tristique et egestas. Blandit aliquam etiam erat velit scelerisque in dictum non consectetur. Id neque aliquam vestibulum morbi blandit cursus risus at. Sed egestas egestas fringilla phasellus faucibus scelerisque eleifend donec. Ornare quam viverra orci sagittis eu volutpat odio facilisis. Volutpat sed cras ornare arcu dui vivamus arcu. Interdum consectetur libero id faucibus nisl.</p>
      <p>Viverra mauris in aliquam sem. Mattis molestie a iaculis at erat pellentesque adipiscing commodo elit. Sit amet volutpat consequat mauris nunc. Aliquam nulla facilisi cras fermentum. Sed turpis tincidunt id aliquet risus feugiat. Augue neque gravida in fermentum et sollicitudin ac orci.</p>
    </div>

    <div class="signature-mark" role="img" aria-label="Handwritten signature of Marcus Elden Vale"></div>
    <div class="signatory">
      <div class="signatory__name">Marcus Elden Vale</div>
      <div class="signatory__title">Chief Director</div>
    </div>

    <footer class="contact-bar">
      <span class="contact-bar__item">
        <svg class="contact-bar__icon" viewBox="0 0 24 24" aria-hidden="true"><path d="M6.6 10.8a15.1 15.1 0 0 0 6.6 6.6l2.2-2.2c.3-.3.7-.4 1-.2 1.1.4 2.3.6 3.6.6.6 0 1 .4 1 1V20c0 .6-.4 1-1 1A17 17 0 0 1 3 4c0-.6.4-1 1-1h3.5c.6 0 1 .4 1 1 0 1.3.2 2.5.6 3.6.1.3 0 .7-.2 1z"/></svg>
        954-218-4650
      </span>
      <span class="contact-bar__item">
        <svg class="contact-bar__icon" viewBox="0 0 24 24" aria-hidden="true"><path d="M6 2h12v5H6zM4 8h16a2 2 0 0 1 2 2v7h-4v5H6v-5H2v-7a2 2 0 0 1 2-2zm4 8v4h8v-4z"/></svg>
        954-582-1346
      </span>
      <span class="contact-bar__item">
        <svg class="contact-bar__icon" viewBox="0 0 24 24" aria-hidden="true"><path d="M2 5h20v14H2zm2 2v.5l8 5 8-5V7z"/></svg>
        info@myrbspine.com
      </span>
      <span class="contact-bar__item">
        <svg class="contact-bar__icon" viewBox="0 0 24 24" aria-hidden="true"><path d="M12 2a7 7 0 0 0-7 7c0 5 7 13 7 13s7-8 7-13a7 7 0 0 0-7-7zm0 9.5A2.5 2.5 0 1 1 12 6.5a2.5 2.5 0 0 1 0 5z"/></svg>
        18735 North Harlow Pkwy, Coral Springs, FL 33071
      </span>
    </footer>
  </article>
</body>
</html>
```